Patent Law

Need to develop a home page for a patent lawyer.

Colors should go with logo, blues...

Company Name- Velric Dunmore, PLLC

Company Overview-

I am an Intellectual Property Lawyer and focus on patents, copyrights, trademarks, & trade secrets. I work with small businesses and start ups in the chemical and biotech industries.

Why Us-

I am small firm that can provide large-firm service at a reasonable price. I also can charge flat-fees for entreprenuers in certain practice areas.

Services-
Intellectual Property
Patents
Copyrights
Trademarks
Trade secrets
Healthcare Compliance
Elder law
Wills
Trusts

Website we like-
http://www.tolvanecrest.com/ - within industry!!
http://www.quarnhollet.com/
http://brevicktallon.com/
http://thegravelwrights.com/

Target Market(s)

My customers will be small business, specifically small start-up companies in the chemical and biotech arena.

Industry/Entity Type

Trade

Requirements
Must have
• Colors should go with logo, blues...

```html
<!DOCTYPE html>
<html lang="en">
<head>
<meta charset="utf-8">
<title>Velric Dunmore, PLLC — Intellectual Property Law</title>
<link href="https://fonts.googleapis.com/css2?family=Open+Sans:wght@400;600;700&display=swap" rel="stylesheet">
<style>
:root{
  --blue:#0a8fd9;
  --blue-deep:#1f6fb5;
  --slate:#4a565e;
  --white:#ffffff;
  --text-grey:#6e6e6e;
  --rule:#c9c9c9;
  --icon-grey:#8a8a8a;
}
*{margin:0;padding:0;box-sizing:border-box}
html,body{width:1200px;height:712px;overflow:hidden;background:var(--white)}
body{font-family:'Open Sans',Arial,sans-serif;position:relative}
.top-band,.bottom-band{position:absolute;left:0;width:1200px;height:4px;background:var(--blue)}
.top-band{top:0}
.bottom-band{bottom:0;height:5px}

.site-header{position:absolute;top:4px;left:0;width:1200px;height:125px}
.brand{position:absolute;left:161px;top:38px;display:flex;align-items:center;gap:10px}
.brand-mark{width:22px;height:22px;border-radius:50%;background:var(--blue-deep)}
.brand-name{font-size:17px;font-weight:600;color:var(--slate);letter-spacing:.5px}

.contact-strip{position:absolute;top:18px;left:829px;display:flex;align-items:center;font-size:13px;color:var(--text-grey)}
.contact-strip .icon-box{width:24px;height:24px;border:1px solid var(--slate);display:flex;align-items:center;justify-content:center;margin-right:11px}
.contact-strip .phone{margin-right:18px}

.main-nav{position:absolute;top:59px;left:482px;width:557px;height:45px;background:var(--blue);display:flex}
.main-nav a{display:flex;align-items:center;padding:0 16px 0 14px;color:var(--white);font-weight:700;font-size:13px;text-decoration:none}
.main-nav a.active{background:var(--slate);padding:0 20px}

.hero{position:absolute;top:129px;left:0;width:1200px;height:464px;
  background:linear-gradient(180deg,#9fb0b8 0%,#6f8c9c 20%,#4e6e80 45%,#6b7b84 70%,#3d4c56 100%)}
.hero-shade{position:absolute;inset:0;background:linear-gradient(90deg,rgba(20,30,38,.45) 0%,rgba(20,30,38,0) 30%,rgba(20,30,38,0) 80%,rgba(20,30,38,.25) 100%)}

.why-us{position:absolute;top:298px;left:161px;width:288px;height:295px;background:var(--slate);color:var(--white)}
.why-us h2{text-align:center;font-size:24px;font-weight:700;margin-top:30px}
.why-us p{font-size:12.2px;line-height:19px;margin:14px 0 0 34px;width:226px}
.btn-more{position:absolute;left:102px;top:232px;width:84px;height:34px;border:1px solid var(--white);display:flex;align-items:center;justify-content:center;font-size:12px;font-weight:700;color:var(--white);text-decoration:none}

.focus-ring{position:absolute;left:768px;top:206px;width:270px;height:270px;border-radius:50%;background:var(--blue-deep);opacity:.9}
.focus-circle{position:absolute;left:774px;top:212px;width:258px;height:258px;border-radius:50%;background:var(--slate);color:var(--white);display:flex;flex-direction:column;align-items:center;justify-content:center;text-align:center}
.focus-circle h3{font-size:20px;font-weight:700;margin-bottom:2px}
.focus-circle p{font-size:16px;line-height:24px}

.cta{position:absolute;top:530px;width:288px;height:63px;background:var(--blue);color:var(--white);font-size:26px;font-weight:700;display:flex;align-items:center;justify-content:center;text-decoration:none}
.cta::before{content:"";position:absolute;top:-12px;left:50%;margin-left:-12px;border-left:12px solid transparent;border-right:12px solid transparent;border-bottom:12px solid var(--blue)}
.cta-services{left:456px}
.cta-contact{left:751px}

.site-footer{position:absolute;top:625px;left:161px;width:878px}
.footer-nav{display:flex;font-size:12.5px;color:var(--text-grey)}
.footer-nav a{color:var(--text-grey);text-decoration:none;padding:0 12px;border-left:1px solid var(--rule);line-height:14px}
.footer-nav a:first-child{padding-left:0;border-left:none}
.copyright{margin-top:9px;font-size:12.5px;color:var(--text-grey)}
.social{position:absolute;right:0;top:2px;display:flex;gap:14px}
.social span{width:18px;height:18px;border-radius:50%;background:var(--icon-grey)}
</style>
</head>
<body>
<div class="top-band"></div>

<header class="site-header">
  <div class="brand">
    <span class="brand-mark"></span>
    <span class="brand-name">VELRIC DUNMORE, PLLC</span>
  </div>
  <div class="contact-strip">
    <span class="icon-box">
      <svg width="12" height="12" viewBox="0 0 24 24"><path fill="#0a8fd9" d="M6.6 10.8c1.4 2.8 3.8 5.1 6.6 6.6l2.2-2.2c.3-.3.7-.4 1-.2 1.1.4 2.3.6 3.6.6.6 0 1 .4 1 1V20c0 .6-.4 1-1 1C10.6 21 3 13.4 3 4c0-.6.4-1 1-1h3.5c.6 0 1 .4 1 1 0 1.3.2 2.5.6 3.6.1.3 0 .7-.2 1z"/></svg>
    </span>
    <span class="phone">+97 990-555-218</span>
    <span class="icon-box">
      <svg width="12" height="13" viewBox="0 0 24 24"><path fill="#0a8fd9" d="M12 2C8.1 2 5 5.1 5 9c0 5.2 7 13 7 13s7-7.8 7-13c0-3.9-3.1-7-7-7zm0 9.5c-1.4 0-2.5-1.1-2.5-2.5S10.6 6.5 12 6.5s2.5 1.1 2.5 2.5-1.1 2.5-2.5 2.5z"/></svg>
    </span>
    <span>Map</span>
  </div>
  <nav class="main-nav">
    <a class="active" href="#">HOME</a>
    <a href="#">ABOUT US</a>
    <a href="#">SERVICES</a>
    <a href="#">PRACTICES</a>
    <a href="#">NEWS</a>
    <a href="#">CONTACT US</a>
  </nav>
</header>

<section class="hero" role="img" aria-label="Panoramic photograph of snow-covered rooftops and church domes over an old European city">
  <div class="hero-shade"></div>
</section>

<article class="why-us">
  <h2>WHY US</h2>
  <p>Lorem Ipsum is simply dummy text of the printing and typesetting industry. Lorem Ipsum has been the industry's standard dummy text ever since the 1500s, when an unknown printer took a galley of type and scrambled it to make a type specimen book.</p>
  <a class="btn-more" href="#">MORE</a>
</article>

<div class="focus-ring"></div>
<div class="focus-circle">
  <h3>i focus On</h3>
  <p>Patents, copyrights,<br>Trademarks &amp; Trade secrets</p>
</div>

<a class="cta cta-services" href="#">SERVICES</a>
<a class="cta cta-contact" href="#">CONTACT US</a>

<footer class="site-footer">
  <nav class="footer-nav">
    <a href="#">Home</a>
    <a href="#">About Us</a>
    <a href="#">Services</a>
    <a href="#">Practices</a>
    <a href="#">News</a>
    <a href="#">Contact us</a>
  </nav>
  <p class="copyright">Copyright © 2014 Velric Dunmore pllc.</p>
  <div class="social"><span></span><span></span><span></span></div>
</footer>

<div class="bottom-band"></div>
</body>
</html>
```